Redesign Website

I currently have a website www.kelvaromotionrx.com that I would like to have redesigned for esthetics and design limitations with the present platform. I will provide my logo, background logo (attached) , current site, foundation grip PSD.zip (attached) and a questionnaire (attached) from a web design company to provide the input to have an impressive site that pleases the eyes and makes an impact. I would also like the site to be mobile friendly.

IMPORTANT:
- The final PSD must include:
o Homepage Mockup
o Internal Pages Mockup
o Mobile site mockup
o Fonts files used in mockup

Final website will be responsive, using the Foundation Framework. Attached you will find a PSD of the Foundation grid – please use this and include with your final PSD. Here is a link for reference:
http://plimtex.com/article/1053/foundation-s-grid-and-photoshop-what-you-

Target Market(s)

Patients for physical therapy

Industry/Entity Type

It Company

Requirements
Must have
• Pages included in the present site. Photos and design should change.
Nice to have
• Should provide information necessary for patients to schedule an appointment
Should not have
• Should not be difficult to read.

```html
<!DOCTYPE html>
<html lang="en">
<head>
<meta charset="utf-8">
<title>Kelvaro Motion Rx Physical Therapy</title>
<link rel="stylesheet" href="https://fonts.googleapis.com/css2?family=Source+Sans+3:wght@400;600&family=Arimo:wght@400&display=swap">
<style>
:root{
  --orange:#e8760f;
  --orange-light:#f39a1c;
  --red:#d21f26;
  --red-dark:#9c1016;
  --text:#444;
  --muted:#5a5a5a;
  --panel-top:#f7f9fa;
  --panel-bottom:#dfe4e8;
  --panel-border:#c9d0d5;
  --footer-top:#5b5b5b;
  --footer-bottom:#1e1e1e;
  --photo-light:#e9e5e2;
  --photo-mid:#a9bdd6;
}
*{box-sizing:border-box;margin:0;padding:0}
html,body{width:1013px;height:1200px;overflow:hidden;background:#fff}
body{position:relative;font-family:"Source Sans 3",Arial,sans-serif;color:var(--text)}
.top-strip{position:absolute;left:0;top:0;width:1013px;height:8px;background:var(--orange)}
.brand{position:absolute;left:46px;top:78px;display:flex;align-items:center;gap:8px}
.brand-dot{width:26px;height:26px;border-radius:50%;background:var(--orange)}
.brand-name{font-size:32px;font-weight:600;color:var(--red);line-height:1}
.brand-sub{position:absolute;left:48px;top:124px;font-size:11.5px;font-weight:600;color:var(--red);letter-spacing:.3px;line-height:13px}
.contact-row{position:absolute;top:44px;left:412px;display:flex;align-items:center;gap:20px;font-size:13px;color:#333;white-space:nowrap}
.contact-item{display:flex;align-items:center;gap:7px}
.social-top{position:absolute;top:38px;left:834px;display:flex;gap:7px}
.social-top span{width:30px;height:31px;border-radius:6px;display:block}
.s-blue{background:#3fa9e0}.s-red{background:#c8262a}.s-navy{background:#3b5a98}.s-teal{background:#1f7fb8}
.main-nav{position:absolute;left:215px;top:98px;width:758px;height:57px;background:linear-gradient(#dc2a2f,#a6131a);border-bottom:5px solid var(--orange);display:flex;align-items:center}
.nav-home{flex:none;width:51px;height:52px;background:linear-gradient(var(--orange-light),var(--orange));display:flex;align-items:center;justify-content:center}
.main-nav ul{list-style:none;display:flex;flex:1;justify-content:space-between;padding:0 4px 0 13px}
.main-nav li{color:#fff;font-size:16.5px;white-space:nowrap;line-height:1}
.hero{position:absolute;left:39px;top:170px;width:934px;height:468px;border:1px solid #ccc;background:linear-gradient(110deg,var(--photo-light) 0%,#f5f2ef 35%,var(--photo-mid) 70%,#d8e1ec 100%)}
.hero-caption{position:absolute;left:0;bottom:0;width:100%;height:50px;background:rgba(40,40,40,.78);color:#fff;font-size:23px;line-height:50px;padding:0 18px;white-space:nowrap}
.hero-dots{position:absolute;right:14px;bottom:14px;display:flex;gap:5px}
.hero-dots span{width:18px;height:18px;border-radius:50%;background:#ddd;border:2px solid #999}
.hero-dots span:first-child{background:#555;border-color:#eee}
.feature{position:absolute;top:651px;width:298px;height:186px;background:linear-gradient(var(--panel-top),var(--panel-bottom));border:1px solid var(--panel-border);text-align:center}
.feature h2{font-weight:400;font-size:21px;color:#444;margin-top:14px;letter-spacing:.3px;white-space:nowrap}
.feature svg{display:block;margin:10px auto 0}
.feature p{font-family:Arimo,Arial,sans-serif;font-size:13.5px;color:#444;line-height:20px;width:236px;margin:14px auto 0;text-align:justify;text-align-last:justify}
.portrait{position:absolute;left:37px;top:876px;width:172px;height:172px;border-radius:50%;border:1px solid #ccc;background:linear-gradient(#c8d5e4,#9fb8d6)}
.bio{position:absolute;left:230px;top:882px;width:426px}
.bio h3{font-size:20px;font-weight:600;color:#333}
.bio p{font-size:12.8px;line-height:20px;color:var(--muted);margin-top:10px;text-align:justify}
.bio .more{color:var(--orange);font-size:12.5px;margin-left:22px;white-space:nowrap}
.schedule{position:absolute;left:676px;top:866px;width:297px;height:212px;background:#eef1f3;border:1px solid #d3d8dc}
.schedule h4{height:34px;background:linear-gradient(#9a9a9a,#7a7a7a);color:#fff;font-size:20px;font-weight:600;text-align:center;line-height:34px;white-space:nowrap}
.appt{position:relative;height:88px;padding:6px 20px;font-size:12.5px;line-height:22px;color:#444;border-bottom:2px solid #d6dbdf;white-space:nowrap}
.appt:last-child{border-bottom:0}
.appt-btn{position:absolute;right:6px;bottom:12px;background:linear-gradient(#d4262c,#a3141a);color:#fff;font-size:12.5px;padding:1px 7px;border-radius:2px;line-height:20px}
.site-footer{position:absolute;left:0;top:1092px;width:1013px;height:108px;background:linear-gradient(var(--footer-top),var(--footer-bottom));color:#fff;font-family:Arimo,Arial,sans-serif;font-size:12.5px}
.copyright{position:absolute;left:40px;top:50px}
.footer-social{position:absolute;left:396px;top:36px;display:flex;gap:9px}
.footer-social span{width:38px;height:38px;border-radius:50%;border:3px solid #444;display:block}
.f1{background:#3fb0e4}.f2{background:#3b5fa8}.f3{background:#666}.f4{background:#e0578b}.f5{background:#eee}
.footer-links{position:absolute;right:40px;top:50px}
</style>
</head>
<body>
<div class="top-strip"></div>

<header>
  <div class="brand"><span class="brand-dot"></span><span class="brand-name">kelvaro</span></div>
  <div class="brand-sub">MOTION RX<br>PHYSICAL THERAPY</div>

  <div class="contact-row">
    <span class="contact-item">
      <svg width="14" height="14" viewBox="0 0 14 14"><rect width="14" height="14" rx="2" fill="#e8760f"/><path d="M4 3l2 2-1 1.5c.6 1.3 1.2 1.9 2.5 2.5L9 8l2 2-1.5 1.5C6 11 3 8 2.5 4.5z" fill="#fff"/></svg>555.201.4470</span>
    <span class="contact-item">
      <svg width="20" height="14" viewBox="0 0 20 14"><rect width="20" height="14" fill="#e8760f"/><path d="M0 0l10 8 10-8" stroke="#fff" stroke-width="1.5" fill="none"/></svg>JMarlow@kelvaromotionrx.com</span>
    <span class="contact-item">
      <svg width="14" height="16" viewBox="0 0 14 16"><circle cx="7" cy="4" r="3.5" fill="#e8760f"/><path d="M0 16c0-5 3-7 7-7s7 2 7 7z" fill="#e8760f"/></svg>Log in</span>
  </div>
  <div class="social-top"><span class="s-blue"></span><span class="s-red"></span><span class="s-navy"></span><span class="s-teal"></span></div>

  <nav class="main-nav">
    <div class="nav-home"><svg width="26" height="24" viewBox="0 0 26 24"><path d="M13 1L1 12h4v11h6v-7h4v7h6V12h4z" fill="#fff"/></svg></div>
    <ul><li>Location</li><li>Hours</li><li>Our Story</li><li>New Patients</li><li>Contact Us</li><li>Testimonials</li><li>Community</li></ul>
  </nav>
</header>

<section class="hero" role="img" aria-label="Therapist in a blue shirt adjusting a knee brace on a patient's leg">
  <div class="hero-caption">Kelvaro Motion Rx Physical Therapy currently supports</div>
  <div class="hero-dots"><span></span><span></span><span></span><span></span></div>
</section>

<section class="feature" style="left:40px">
  <h2>SERVICES</h2>
  <svg width="64" height="62" viewBox="0 0 64 62"><circle cx="22" cy="40" r="12" fill="none" stroke="#e8760f" stroke-width="9" stroke-dasharray="5 3.6"/><circle cx="22" cy="40" r="9" fill="#e8760f"/><circle cx="22" cy="40" r="4" fill="#eef1f3"/><circle cx="46" cy="16" r="8" fill="none" stroke="#f39a1c" stroke-width="7" stroke-dasharray="4 2.5"/><circle cx="46" cy="16" r="6" fill="#f39a1c"/><circle cx="46" cy="16" r="3" fill="#eef1f3"/></svg>
  <p>Aenean nonummy hendrerit mauris. Phasellus porta. Fusce suscipit varius</p>
</section>
<section class="feature" style="left:358px">
  <h2>INSURANCE</h2>
  <svg width="66" height="62" viewBox="0 0 66 62"><circle cx="44" cy="20" r="9" fill="#e8760f"/><path d="M30 58c0-18 6-24 14-24s14 6 14 24z" fill="#e8760f"/><circle cx="26" cy="16" r="11" fill="#f39a1c"/><path d="M6 60c0-22 8-30 20-30s20 8 20 30z" fill="#f39a1c"/></svg>
  <p>Aenean nonummy hendrerit mauris. Phasellus porta. Fusce suscipit varius</p>
</section>
<section class="feature" style="left:676px">
  <h2>MISSION STATEMENT</h2>
  <svg width="72" height="62" viewBox="0 0 72 62"><rect x="4" y="2" width="64" height="56" fill="#e8760f"/><rect x="9" y="8" width="54" height="44" fill="#fbe3c5"/><rect x="13" y="13" width="46" height="6" fill="#e8760f"/><rect x="13" y="23" width="18" height="20" fill="#e8760f"/><rect x="35" y="24" width="24" height="4" fill="#e8760f"/><rect x="35" y="32" width="24" height="4" fill="#e8760f"/><rect x="35" y="40" width="24" height="4" fill="#e8760f"/></svg>
  <p>Aenean nonummy hendrerit mauris. Phasellus porta. Fusce suscipit varius</p>
</section>

<div class="portrait" role="img" aria-label="Portrait photo of the lead physical therapist"></div>
<article class="bio">
  <h3>Jon Marlow, PT, DPT, MS</h3>
  <p>Our services are the culmination of 15 years of experience of Dr. Jon Marlow, PT, DPT, MS in the sports and orthopedic physical therapy arena. Jon directed the rehabilitation services for the largest orthopedic group in Alder County. He has provided the services for an orthopedic and sports medicine group that had specialists in spine, shoulder, elbow, wrist, hand, hip, knee, ankle and foot surgery and treatment. His expertise is the treatment of any and all sports and orthopedic injuries, whether they are the result of trauma, <span class="more">READ MORE &gt;&gt;</span></p>
</article>

<aside class="schedule">
  <h4>Schedule Your Appointment!</h4>
  <div class="appt">Kelvaro Motion Rx Physical Therapy<br>218 Orchard Avenue<br>Suite 4 , Brookfield, Pa 19400<span class="appt-btn">APPOINTMENT!</span></div>
  <div class="appt">Kelvaro Motion Rx Physical Therapy<br>218 Orchard Avenue<br>Suite 4 , Brookfield, Pa 19400<span class="appt-btn">APPOINTMENT!</span></div>
</aside>

<footer class="site-footer">
  <div class="copyright">© Kelvaro Motion Rx Physical Therapy</div>
  <div class="footer-social"><span class="f1"></span><span class="f2"></span><span class="f3"></span><span class="f4"></span><span class="f5"></span></div>
  <div class="footer-links">Print | Sitemap | Login</div>
</footer>
</body>
</html>
```